Business Card for Voltrix

Horizontal business card for voltrix, the electrical contractor.
clean and professional looking, using company branding and colours.
I also want the blue in the logo and wording to be made a more 'electric' blue and the grey 'Voltrix' to be slightly darker.

Pleas use the following contact details:

Colin Marsh
Owner

t: 01736 582910
m: 07831 206719
e: colin@voltrix-installs.co.uk

www.voltrix-installs.co.uk

Industry/Entity Type

Electrical

Font styles to use
Sans Serif

```html
<!DOCTYPE html>
<html lang="en">
<head>
<meta charset="utf-8">
<title>Voltrix Business Card – Front Side</title>
<link rel="stylesheet" href="https://fonts.googleapis.com/css2?family=Arimo:wght@400;500;700&display=swap">
<style>
  :root {
    --canvas-bg: #ffffff;
    --card-bg: #ffffff;
    --card-border: #1a1a1a;
    --brand-blue: #00aeef;
    --brand-grey: #7e8182;
    --brand-mark: #9fcfd0;
    --ink: #111111;
  }
  html, body {
    margin: 0;
    padding: 0;
    width: 1200px;
    height: 1000px;
    overflow: hidden;
    background: var(--canvas-bg);
    font-family: "Arimo", Arial, sans-serif;
    color: var(--ink);
  }
  .stage {
    position: relative;
    width: 1200px;
    height: 1000px;
  }
  .card {
    position: absolute;
    left: 87px;
    top: 173px;
    width: 1020px;
    height: 567px;
    box-sizing: border-box;
    border: 1.5px solid var(--card-border);
    background: var(--card-bg);
  }
  .brand {
    position: absolute;
    left: 150px;
    top: 84px;
    display: flex;
    align-items: center;
    gap: 22px;
  }
  .brand-dot {
    width: 82px;
    height: 82px;
    border-radius: 50%;
    background: var(--brand-mark);
    flex: none;
  }
  .brand-text {
    display: flex;
    flex-direction: column;
  }
  .brand-name {
    font-size: 78px;
    font-weight: 500;
    line-height: 1;
    letter-spacing: 26px;
    color: var(--brand-grey);
    text-transform: uppercase;
  }
  .brand-tagline {
    margin-top: 6px;
    font-size: 29px;
    font-weight: 400;
    letter-spacing: 2.5px;
    line-height: 1;
    color: var(--brand-blue);
    text-transform: uppercase;
  }
  .person {
    position: absolute;
    left: 0;
    right: 0;
    top: 266px;
    text-align: center;
  }
  .person-name {
    margin: 0;
    font-size: 44px;
    font-weight: 500;
    line-height: 1.05;
    color: var(--brand-blue);
  }
  .person-role {
    margin: 0;
    font-size: 30px;
    font-weight: 400;
    line-height: 1.2;
    color: var(--ink);
  }
  .contacts {
    position: absolute;
    left: 0;
    right: 0;
    top: 425px;
    font-size: 26px;
    line-height: 1;
  }
  .contact-row {
    display: flex;
    justify-content: center;
    align-items: center;
    gap: 10px;
  }
  .contact-row + .contact-row { margin-top: 16px; }
  .contact-item {
    display: inline-flex;
    align-items: center;
    gap: 10px;
  }
  .contact-item + .contact-item { margin-left: 14px; }
  .icon { flex: none; }
  .separator { margin: 0 4px; }
  .side-label {
    position: absolute;
    left: 0;
    right: 0;
    top: 798px;
    text-align: center;
    font-size: 36px;
    font-weight: 500;
    letter-spacing: 0.5px;
    color: var(--ink);
  }
</style>
</head>
<body>
  <main class="stage">
    <section class="card" aria-label="Business card front">
      <div class="brand">
        <span class="brand-dot" aria-hidden="true"></span>
        <div class="brand-text">
          <span class="brand-name">Voltrix</span>
          <span class="brand-tagline">The Electrical Contractor</span>
        </div>
      </div>

      <div class="person">
        <h1 class="person-name">Colin Marsh</h1>
        <p class="person-role">Owner</p>
      </div>

      <div class="contacts">
        <div class="contact-row">
          <span class="contact-item">
            <svg class="icon" width="34" height="34" viewBox="0 0 34 34" aria-hidden="true">
              <circle cx="17" cy="17" r="15.5" fill="none" stroke="var(--brand-blue)" stroke-width="2"/>
              <path d="M12 9c-1.5 1-2.5 2.5-2 4.5 1 4 5.5 9.5 9.5 11 2 .7 3.5 0 4.5-1.5l-3-3-2 1.2c-2-1-4-3.5-5-5.5l1.3-2z" fill="none" stroke="var(--brand-blue)" stroke-width="1.8" stroke-linejoin="round"/>
            </svg>
            01736 582910
          </span>
          <span class="contact-item">
            <svg class="icon" width="22" height="36" viewBox="0 0 22 36" aria-hidden="true">
              <rect x="1.5" y="1.5" width="19" height="33" rx="3" fill="none" stroke="var(--brand-blue)" stroke-width="2.2"/>
              <line x1="1.5" y1="28" x2="20.5" y2="28" stroke="var(--brand-blue)" stroke-width="1.8"/>
              <circle cx="11" cy="31.3" r="1.2" fill="var(--brand-blue)"/>
            </svg>
            07831 206719
          </span>
        </div>
        <div class="contact-row">
          <span class="contact-item">
            <svg class="icon" width="30" height="22" viewBox="0 0 30 22" aria-hidden="true">
              <rect x="1" y="1" width="28" height="20" fill="none" stroke="var(--brand-blue)" stroke-width="2"/>
              <path d="M1 1l14 11L29 1M1 21l10-10M29 21L19 11" fill="none" stroke="var(--brand-blue)" stroke-width="2"/>
            </svg>
            <span>colin@voltrix-installs.co.uk</span>
          </span>
          <span class="separator">•</span>
          <span>www.voltrix-installs.co.uk</span>
        </div>
      </div>
    </section>

    <p class="side-label">FRONT SIDE</p>
  </main>
</body>
</html>
```